Magento e-commerce webdesign

We need a full e-commerce design for a company based in France. The website will sell belts (men / women).
In files, you have our logo. We made a try for a brown visit card, but it's just an idea. The brown color can be used if it looks like leather, warning it MUSN'T look like "brown shit" :)
So you are free with color but never forget we sell belts and it's both for men & women (upmarket). You can make your own colors changes on the logo (only colors).
You'll find 2 wireframes with the home page & the category page. Elements are in french. UPDATED : you have a traduction files, but it would better if you can make it in french.
Photos have to be on a white background.
Carroussel & every pictures of the wireframes area are very importants.
Target Market(s)
Men & women
Fashion peoples
Upmarket
Industry/Entity Type
It Company
Requirements
Must have
- work on the colors
- work on the pictures (carroussel, newsletter, ventes privées, services, category)
- pro & upmarket
Nice to have
- Product detail page
- Texts in french
Should not have
- Shitty brown colors

```html
<!DOCTYPE html>
<html lang="en">
<head>
<meta charset="utf-8">
<title>cuirelle — belts for men and women</title>
<link href="https://fonts.googleapis.com/css2?family=Arimo:wght@400;700&family=Marcellus&display=swap" rel="stylesheet">
<style>
  :root {
    --leather-dark: #2f170b;
    --leather: #4a2412;
    --leather-warm: #5c2f18;
    --nav: #3a1b0c;
    --caramel: #7a4a22;
    --subscribe: #a0612a;
    --grey-head: #9b9b9b;
    --grey-band: #bab5b1;
    --teal: #2b6375;
    --ink: #1c1410;
    --muted: #555;
    --card: #f0f0f0;
    --white: #fff;
  }
  * { box-sizing: border-box; margin: 0; padding: 0; }
  html, body { width: 943px; height: 1200px; overflow: hidden; background: var(--white); }
  body { position: relative; font-family: "Arimo", Arial, sans-serif; color: var(--ink); }
  .abs { position: absolute; }

  /* header */
  .site-header { left: 0; top: 0; width: 943px; height: 137px;
    background: radial-gradient(ellipse at 45% 40%, #5a2c16 0%, var(--leather) 45%, var(--leather-dark) 100%); }
  .brand { left: 70px; top: 38px; display: flex; align-items: center; gap: 10px; }
  .brand-mark { width: 14px; height: 14px; border-radius: 50%; background: #d9d4d0; }
  .brand-name { font-family: "Marcellus", serif; font-size: 42px; color: #d9d4d0; letter-spacing: 1px; }
  .cart { left: 671px; top: 27px; width: 226px; height: 72px; border-radius: 8px;
    background: rgba(20, 8, 3, .55); }
  .cart-count { left: 13px; top: 23px; font-size: 10px; color: #cfc6c0; }
  .cart-total { left: 13px; top: 41px; font-size: 12.5px; color: #d8d0ca; }
  .cart-total b { color: #fff; }
  .cart-icon { left: 171px; top: 12px; }

  .main-nav { left: 0; top: 137px; width: 943px; height: 33px;
    background: linear-gradient(#5a2c15, var(--nav) 60%, #6a3a20); }
  .main-nav a { position: absolute; top: 9px; font-size: 12.5px; color: #f1e7df; text-decoration: none; }

  /* hero */
  .hero { left: 43px; top: 178px; width: 576px; height: 330px;
    background: linear-gradient(90deg, #eae0d9 0%, #c9b8ad 35%, #c1afa4 70%, #d8cbc3 100%); }
  .hero-photo { left: 0; top: 0; width: 576px; height: 330px; }
  .hero-title { left: 244px; top: 44px; width: 330px; font-size: 30px; line-height: 31px; color: #2a1c14; }
  .hero-cta { left: 386px; top: 253px; width: 145px; height: 39px; background: #2b1a10;
    color: #fff; font-size: 19px; display: flex; align-items: center; gap: 10px; padding-left: 12px; }

  /* sidebar promos */
  .promo { left: 626px; width: 274px; overflow: hidden; }
  .promo-head { height: 32px; padding: 6px 9px; font-family: "Marcellus", serif; font-size: 18px; color: #fff; }
  .promo-body { font-size: 10px; line-height: 15.5px; }
  .newsletter { top: 178px; height: 105px; background: linear-gradient(var(--leather-warm), #6d3a1f); }
  .newsletter .promo-head { background: var(--caramel); }
  .newsletter p { position: absolute; left: 18px; top: 44px; font-size: 10px; color: #fff; }
  .email-field { left: 13px; top: 66px; width: 156px; height: 19px; background: #fff;
    font-size: 10px; color: #888; padding: 3px 8px; }
  .subscribe { left: 181px; top: 66px; width: 81px; height: 19px; background: var(--subscribe);
    color: #fff; font-size: 11.5px; text-align: center; line-height: 19px; }
  .private-sales { top: 291px; height: 104px; background: #e9e7e6; }
  .private-sales .promo-head { background: var(--grey-head); }
  .services { top: 403px; height: 105px; background: linear-gradient(90deg, #cfe3ea, #a9ccd7); }
  .services .promo-head { background: var(--teal); }
  .promo-visual { position: absolute; right: 0; top: 32px; bottom: 0; }
  .promo-text { position: absolute; left: 10px; top: 42px; width: 160px; color: #4a4a4a; }

  /* products */
  .section-title { left: 53px; top: 524px; font-size: 18px; color: #111; }
  .product { top: 567px; width: 156px; height: 234px; text-align: center; }
  .product-photo { width: 156px; height: 185px; background: radial-gradient(circle at 50% 55%, #dcdcdc, var(--card) 70%); }
  .product-name { margin-top: 7px; font-size: 12.5px; }
  .product-price { margin-top: 7px; font-size: 11px; }
  .product.is-active { border: 1px solid #222; }
  .product.is-active .product-photo { height: 184px; }
  .product.is-active .product-info { background: var(--leather-dark); color: #fff; height: 48px; padding-top: 1px; }

  /* footer */
  .footer { left: 43px; top: 831px; width: 856px; height: 317px; background: var(--leather-dark); }
  .assurance-band { left: 0; top: 66px; width: 856px; height: 52px; background: var(--grey-band); }
  .assurance { top: 23px; width: 180px; height: 75px; border-radius: 6px;
    background: linear-gradient(#fff, #e2e2e2); }
  .assurance h3 { position: absolute; left: 10px; top: 8px; font-weight: 400; font-size: 13px; color: #333; }
  .assurance .rule { position: absolute; left: 10px; right: 58px; top: 27px; border-top: 1px solid #bbb; }
  .assurance p { position: absolute; left: 0; right: 0; top: 41px; font-size: 10px; line-height: 15px; color: #444; text-align: center; }
  .assurance .icon { position: absolute; right: 12px; top: 7px; }
  .blog-title, .follow-title { top: 140px; font-size: 19px; color: #fff; }
  .footer-rule { left: 0; top: 170px; width: 856px; border-top: 1px solid #5a3524; }
  .blog-entry { left: 20px; width: 440px; height: 36px; display: flex; gap: 18px; align-items: center; }
  .blog-thumb { width: 66px; height: 36px; background: #fff; border: 2px solid #7a3a22; flex: none; }
  .blog-entry p { font-size: 10px; line-height: 13px; color: #fff; }
  .more { left: 405px; top: 293px; font-size: 9.5px; font-weight: 700; color: #fff; }
  .divider { left: 485px; top: 180px; height: 115px; border-left: 1px solid #1c0c05; }
  .social { left: 563px; width: 128px; height: 18px; display: flex; align-items: center; gap: 8px;
    padding-left: 5px; font-size: 9.5px; font-weight: 700; border-radius: 2px; }
  .social span.dot { width: 9px; height: 9px; background: #fff; opacity: .8; }
  .social.chirper { top: 173px; background: #9fdbea; color: #2d6f86; }
  .social.chirper span.dot { background: #2d8fb0; }
  .social.friendly { top: 205px; background: #3e5d9a; color: #fff; }

  .legal { top: 1152px; font-size: 10.5px; color: #555; }
</style>
</head>
<body>

<header class="site-header abs">
  <div class="brand abs"><span class="brand-mark"></span><span class="brand-name">cuirelle</span></div>
  <div class="cart abs">
    <span class="cart-count abs">There is 2 items in your cart</span>
    <span class="cart-total abs">Cart Subtotal: <b>$ 999.99</b></span>
    <svg class="cart-icon abs" width="40" height="40" viewBox="0 0 40 40" aria-hidden="true">
      <path d="M4 10 h6 l5 17 h17 l4 -12 h-23" fill="none" stroke="#f0a72a" stroke-width="3" stroke-linejoin="round"/>
      <circle cx="17" cy="33" r="3" fill="#ddd"/><circle cx="30" cy="33" r="3" fill="#ddd"/>
      <path d="M23 3 v12 M17 9 h12" stroke="#7cc242" stroke-width="4"/>
    </svg>
  </div>
</header>

<nav class="main-nav abs">
  <a href="#" style="left:66px">Men</a>
  <a href="#" style="left:119px">Women</a>
  <a href="#" style="left:192px">Accessories</a>
  <a href="#" style="left:728px">My account</a>
  <a href="#" style="left:819px">Sponsorship</a>
</nav>

<section class="hero abs">
  <svg class="hero-photo abs" role="img" aria-label="Model in a red summer dress wearing a brown leather belt" width="576" height="330">
    <rect x="55" y="10" width="90" height="320" fill="#cfa99b" opacity=".35"/>
  </svg>
  <h1 class="hero-title abs" style="font-weight:400">Lorem ipsum dolor sit amet, consectetuer adipiscing elit. Aenean commodo ligula eget dolor.</h1>
  <a class="hero-cta abs" href="#">
    <svg width="20" height="16" viewBox="0 0 20 16" aria-hidden="true"><path d="M2 2 l6 6 l-6 6 M10 2 l6 6 l-6 6" fill="none" stroke="#fff" stroke-width="2.6"/></svg>
    See more
  </a>
</section>

<aside class="promo newsletter abs">
  <div class="promo-head">Newsletter</div>
  <p>Sign up for our newsletter.</p>
  <div class="email-field abs">Email</div>
  <div class="subscribe abs">Subscribe</div>
</aside>

<aside class="promo private-sales abs">
  <div class="promo-head">Private sales</div>
  <div class="promo-text promo-body">Lorem ipsum dolor sit amet, consectetuer adipiscing elit. Aenean&nbsp; dolor.</div>
  <svg class="promo-visual" width="120" height="72" role="img" aria-label="Red leather belt with a silver buckle">
    <rect width="120" height="72" fill="url(#ps)"/>
    <defs><linearGradient id="ps" x1="0" x2="1"><stop offset="0" stop-color="#e9e7e6"/><stop offset="1" stop-color="#c4202a"/></linearGradient></defs>
  </svg>
</aside>

<aside class="promo services abs">
  <div class="promo-head">Discover our services</div>
  <div class="promo-text promo-body" style="width:170px">Lorem ipsum dolor sit amet, consectetuer adipiscing elit. Aenean</div>
  <svg class="promo-visual" width="100" height="73" role="img" aria-label="Customer service advisor wearing a headset">
    <rect width="100" height="73" fill="url(#sv)"/>
    <defs><linearGradient id="sv" x1="0" x2="1"><stop offset="0" stop-color="#a9ccd7" stop-opacity="0"/><stop offset=".5" stop-color="#d9b8a6"/><stop offset="1" stop-color="#8a6a58"/></linearGradient></defs>
  </svg>
</aside>

<h2 class="section-title abs" style="font-weight:400">New Products</h2>

<article class="product is-active abs" style="left:43px">
  <div class="product-photo" role="img" aria-label="Striped canvas belt with round metal buckle"></div>
  <div class="product-info"><div class="product-name">Lorem ipsum</div><div class="product-price">$ 111</div></div>
</article>
<article class="product abs" style="left:219px">
  <div class="product-photo" role="img" aria-label="Black leather belt with double-prong buckle"></div>
  <div class="product-info"><div class="product-name">Lorem ipsum</div><div class="product-price">$ 111</div></div>
</article>
<article class="product abs" style="left:393px">
  <div class="product-photo" role="img" aria-label="Striped canvas belt with round metal buckle"></div>
  <div class="product-info"><div class="product-name">Lorem ipsum</div><div class="product-price">$ 111</div></div>
</article>
<article class="product abs" style="left:567px">
  <div class="product-photo" role="img" aria-label="Striped canvas belt with round metal buckle"></div>
  <div class="product-info"><div class="product-name">Lorem ipsum</div><div class="product-price">$ 111</div></div>
</article>
<article class="product abs" style="left:741px">
  <div class="product-photo" role="img" aria-label="Striped canvas belt with round metal buckle"></div>
  <div class="product-info"><div class="product-name">Lorem ipsum</div><div class="product-price">$ 111</div></div>
</article>

<footer class="footer abs">
  <div class="assurance-band abs"></div>

  <div class="assurance abs" style="left:24px">
    <h3>Payment</h3><div class="rule"></div>
    <svg class="icon" width="32" height="20" aria-hidden="true"><rect x="1" y="2" width="30" height="16" rx="2" fill="#8a8a8a"/><rect x="4" y="6" width="24" height="8" fill="#eee"/></svg>
    <svg class="abs" style="left:13px;top:42px" width="110" height="14" aria-hidden="true">
      <rect x="0" y="1" width="20" height="12" rx="1" fill="#2a4c9a"/>
      <rect x="26" y="1" width="20" height="12" rx="1" fill="#d9502a"/>
      <rect x="52" y="1" width="20" height="12" rx="1" fill="#2a4c9a"/>
      <rect x="78" y="1" width="20" height="12" rx="1" fill="#d9502a"/>
    </svg>
  </div>

  <div class="assurance abs" style="left:230px">
    <h3>Delivery</h3><div class="rule"></div>
    <svg class="icon" width="40" height="28" aria-hidden="true"><rect x="1" y="4" width="24" height="16" fill="#9a9a9a"/><path d="M25 9 h8 l5 6 v5 h-13z" fill="#777"/><circle cx="9" cy="22" r="4" fill="#444"/><circle cx="31" cy="22" r="4" fill="#444"/></svg>
    <p style="text-align:left;left:14px;top:36px">Your order shipped<br>with in 48h</p>
  </div>

  <div class="assurance abs" style="left:437px">
    <h3>Service</h3><div class="rule"></div>
    <svg class="icon" width="28" height="28" aria-hidden="true"><circle cx="14" cy="14" r="13" fill="#6a6a6a"/><circle cx="14" cy="14" r="5" fill="none" stroke="#fff" stroke-width="2"/><path d="M19 14 v2 a3 3 0 0 0 5 0 v-2 a10 10 0 1 0 -4 8" fill="none" stroke="#fff" stroke-width="2"/></svg>
    <p>xxxxx@xxxx.com<br>Phone and e-mail</p>
  </div>

  <div class="assurance abs" style="left:643px">
    <h3>Guarantee</h3><div class="rule"></div>
    <svg class="icon" width="32" height="30" aria-hidden="true"><rect x="6" y="2" width="24" height="26" fill="#e4e4e4" stroke="#bbb"/><circle cx="9" cy="12" r="6" fill="#999"/></svg>
    <p style="top:36px">Warrenty 10 days&nbsp; OR<br>Money back</p>
  </div>

  <h2 class="blog-title abs" style="left:20px;font-weight:400">Latest blog entries</h2>
  <h2 class="follow-title abs" style="left:563px;font-weight:400">Follow us</h2>
  <div class="footer-rule abs"></div>

  <div class="blog-entry abs" style="top:161px"><div class="blog-thumb"></div><p>Lorem ipsum dolor sit amet, consectetuer adipiscing elit. Aenean commodo ligula eget dolor.</p></div>
  <div class="blog-entry abs" style="top:205px"><div class="blog-thumb"></div><p>Lorem ipsum dolor sit amet, consectetuer adipiscing elit. Aenean commodo ligula eget dolor.</p></div>
  <div class="blog-entry abs" style="top:251px"><div class="blog-thumb"></div><p>Lorem ipsum dolor sit amet, consectetuer adipiscing elit. Aenean commodo ligula eget dolor.</p></div>
  <span class="more abs">more</span>
  <div class="divider abs"></div>

  <a class="social chirper abs" href="#"><span class="dot"></span>Sign in with Chirper</a>
  <a class="social friendly abs" href="#"><span class="dot"></span>Sign in with Friendly</a>
</footer>

<span class="legal abs" style="left:48px">CGV</span>
<span class="legal abs" style="left:85px">CGU</span>
<span class="legal abs" style="left:118px">sitemap</span>
<span class="legal abs" style="left:855px">crédits</span>

</body>
</html>
```